Harborline Energy - needs a business card

Harborline Energy is a U.S. based diesel sourcing and distribution company that supports American oil & gas fields through providing quality product and consistent services.

Target Market(s)

Oil and Gas

Contact Information for Business Card

The background of the card must be white to ensure the logo pops.

Font styles to use
Serif
Sans Serif

Colors

Designer to choose colors to be used in the design.

Requirements
Must have
• Front of Card: Tag line: Harborline Energy, Powering America's Oil & Gas fields.
• Not sure if you guys do this part but just in case...
• Dale Menschow
• Owner/CEO
• C:555.318.4076
• E:Dmenschow@harborlineenergy.example
• W:Harborlineenergy.example
• Locations: Servicing the Powder River, DJ basin and Bakken formations.
• Back of Card: " Frac fueling is what we do. We understand how important diesel fuel is to your operation, which is why our main service line is Frac fueling. We assure our supply and stand by our service"

```html
<!DOCTYPE html>
<html lang="en">
<head>
<meta charset="utf-8">
<title>Harborline Energy – Business Card</title>
<link href="https://fonts.googleapis.com/css2?family=Audiowide&family=Michroma&family=Josefin+Sans:wght@300;400;600;700&display=swap" rel="stylesheet">
<style>
  :root {
    --navy: #1b2a5c;
    --red: #c1272d;
    --white: #ffffff;
    --stage: #eef0f2;
    --soft-white: #e9ecf4;
  }
  * { margin: 0; padding: 0; box-sizing: border-box; }
  html, body { width: 1200px; height: 622px; overflow: hidden; background: var(--stage); }
  .canvas { position: relative; width: 1200px; height: 622px; }

  .card { position: absolute; top: 149px; width: 520px; height: 324px; overflow: hidden; }

  /* Front */
  .card-front { left: 71px; background: var(--white); box-shadow: 0 2px 6px rgba(0,0,0,.12); }
  .front-bar { position: absolute; height: 7px; background: var(--navy); top: 0; }
  .front-bar.left { left: 0; width: 187px; }
  .front-bar.right { right: 0; width: 187px; }
  .front-bar.bottom { top: auto; bottom: 0; left: 0; width: 100%; background: var(--red); }
  .front-brand {
    position: absolute; left: 0; right: 0; top: 110px;
    display: flex; align-items: center; justify-content: center; gap: 14px;
  }
  .brand-dot { width: 30px; height: 30px; border-radius: 50%; background: var(--navy); }
  .front-brand .brand-name {
    font-family: 'Josefin Sans', sans-serif; font-weight: 700; font-size: 30px;
    letter-spacing: 2px; color: var(--navy); text-transform: uppercase;
  }
  .front-tagline {
    position: absolute; left: 0; right: 0; top: 248px; text-align: center;
    font-family: 'Michroma', sans-serif; font-size: 15px; color: var(--red);
    letter-spacing: .5px; text-transform: uppercase;
  }

  /* Back */
  .card-back { left: 609px; background: var(--navy); color: var(--white); font-family: 'Josefin Sans', sans-serif; font-weight: 300; }
  .back-brand {
    position: absolute; left: 20px; width: 230px; top: 58px;
    display: flex; flex-direction: column; align-items: center; gap: 10px;
  }
  .back-brand .brand-dot { width: 44px; height: 44px; background: var(--white); }
  .back-brand .brand-name { font-weight: 600; font-size: 15px; letter-spacing: 1.5px; text-transform: uppercase; color: var(--white); }
  .mission {
    position: absolute; left: 20px; width: 230px; top: 148px; text-align: center; line-height: 1.5;
  }
  .mission .small { font-size: 10.5px; }
  .mission .mid { font-size: 12.5px; }
  .mission .service { font-weight: 600; font-size: 14px; margin-top: 5px; }
  .divider { position: absolute; left: 255px; top: 72px; width: 1px; height: 183px; background: var(--soft-white); }
  .contact { position: absolute; right: 26px; top: 70px; text-align: right; }
  .contact-name { font-family: 'Audiowide', sans-serif; font-style: italic; font-size: 21px; color: var(--red); }
  .contact-role { font-size: 13px; margin-top: 3px; }
  .contact-phone { font-size: 14px; margin-top: 14px; }
  .contact-email { font-size: 11.5px; margin-top: 6px; }
  .locations { position: absolute; left: 282px; top: 190px; font-size: 11.5px; line-height: 1.4; }
  .website { position: absolute; left: 282px; top: 236px; font-size: 13px; letter-spacing: .3px; }
  .promise {
    position: absolute; left: 0; right: 0; top: 278px; text-align: center;
    font-size: 14px; letter-spacing: .4px; text-transform: uppercase;
  }
</style>
</head>
<body>
<main class="canvas">
  <section class="card card-front" aria-label="Card front">
    <div class="front-bar left"></div>
    <div class="front-bar right"></div>
    <div class="front-brand">
      <span class="brand-dot"></span>
      <span class="brand-name">Harborline Energy</span>
    </div>
    <p class="front-tagline">Powering America's Oil &amp; Gas Fields</p>
    <div class="front-bar bottom"></div>
  </section>

  <section class="card card-back" aria-label="Card back">
    <div class="back-brand">
      <span class="brand-dot"></span>
      <span class="brand-name">Harborline Energy</span>
    </div>
    <div class="mission">
      <p class="small">We understand how important</p>
      <p class="mid">DIESEL FUEL IS TO YOUR OPERATION,</p>
      <p class="small">which is why our main service line is</p>
      <p class="service">FRAC FUELING</p>
    </div>
    <div class="divider"></div>
    <div class="contact">
      <p class="contact-name">Dale Menschow</p>
      <p class="contact-role">Owner | CEO</p>
      <p class="contact-phone">555.318.4076</p>
      <p class="contact-email">Dmenschow@harborlineenergy.example</p>
    </div>
    <p class="locations">Servicing the Powder River,<br>DJ basin and Bakken formations.</p>
    <p class="website">HARBORLINEENERGY.EXAMPLE</p>
    <p class="promise">We assure our supply and stand by our service</p>
  </section>
</main>
</body>
</html>
```